Coffeeshop menu for filter tip

We want to have a cannabis (coffeeshop) menu in the size 25mm wide x 60mm wide. Some examples attached.

it must have the following text:
Menu

WEED p/g
Velotrine €16
Cinderfox €14
Tide Rambler €14
Marigolden €16
Grand Pelican €14
Copper Comet €14

HASH p/g
Baltic Ember €12
Harbor Velvet€11
Plum Rova €14
Dusk Maple €10

Target Market(s)

tourist in Amsterdam

Requirements
Nice to have
• cannabis sign leaf
• No Cigarettes allowed symbol

```html
<!DOCTYPE html>
<html lang="en">
<head>
<meta charset="utf-8">
<title>Amsterdam Menu</title>
<link rel="stylesheet" href="https://fonts.googleapis.com/css2?family=Cinzel:wght@700;900&family=Montserrat:wght@400;500&family=Roboto+Condensed:wght@700&display=swap">
<style>
  :root {
    --page-bg: #e9e4da;
    --card-bg: #4b3b0d;
    --card-bg-dark: #3f3109;
    --leaf-tone: #5e5016;
    --line: #f1ead8;
    --text: #fbf6ea;
    --accent: #f4a11b;
    --no-smoke: #e2384a;
  }
  * { margin: 0; padding: 0; box-sizing: border-box; }
  html, body { width: 1200px; height: 1200px; overflow: hidden; }
  body { background: var(--page-bg); position: relative; }

  .menu-card {
    position: absolute; left: 369px; top: 45px;
    width: 462px; height: 1110px;
    background: linear-gradient(180deg, var(--card-bg-dark) 0%, var(--card-bg) 35%, var(--card-bg) 100%);
    box-shadow: 0 6px 24px rgba(0,0,0,.25);
    color: var(--text);
    font-family: "Montserrat", sans-serif;
  }
  .leaf-decoration {
    position: absolute; left: 20px; top: 270px; width: 420px; height: 800px;
    background: radial-gradient(ellipse at 55% 50%, var(--leaf-tone) 0%, rgba(94,80,22,.35) 45%, rgba(94,80,22,0) 72%);
    opacity: .7;
  }
  .frame { position: absolute; inset: 0; width: 462px; height: 1110px; }

  .title {
    position: absolute; left: 0; width: 100%; top: 112px; text-align: center;
    font-family: "Cinzel", serif; font-weight: 900; font-size: 44px; letter-spacing: 0.5px;
    line-height: 1;
  }
  .title .cap { font-size: 52px; }
  .subtitle {
    position: absolute; left: 0; width: 100%; top: 175px; text-align: center;
    font-family: "Montserrat", sans-serif; font-weight: 500; font-size: 56px;
    letter-spacing: 18px; padding-left: 18px; color: var(--accent); line-height: 1;
  }
  .rule {
    position: absolute; left: 57px; width: 348px; height: 2px;
    background: linear-gradient(90deg, rgba(241,234,216,0), var(--line) 20%, var(--line) 80%, rgba(241,234,216,0));
    opacity: .75;
  }
  .rule--top { top: 246px; }
  .rule--middle { top: 683px; }

  .section-head {
    position: absolute; left: 0; width: 100%;
    font-family: "Roboto Condensed", sans-serif; font-weight: 700; font-size: 29px; line-height: 1;
  }
  .section-head span { position: absolute; top: 0; }
  .section-head .label { left: 60px; }
  .section-head .unit { left: 250px; }
  .section-head--weed { top: 325px; }
  .section-head--hash { top: 740px; }
  .section-head--hash .label { left: 63px; }
  .section-head--hash .unit { left: 259px; }

  .head-line { position: absolute; height: 1px; background: var(--line); opacity: .45; }
  .head-line--weed-a { top: 361px; left: 40px; width: 125px; }
  .head-line--weed-b { top: 361px; left: 250px; width: 130px; }
  .head-line--hash-a { top: 780px; left: 45px; width: 125px; }
  .head-line--hash-b { top: 780px; left: 255px; width: 130px; }

  .price-list { list-style: none; position: absolute; left: 0; width: 100%; }
  .price-list li { position: absolute; left: 0; width: 100%; height: 30px; font-size: 28px; line-height: 30px; }
  .price-list .name { position: absolute; left: 47px; white-space: nowrap; }
  .price-list .price { position: absolute; left: 296px; color: var(--accent); font-weight: 500; }

  .footer-note {
    position: absolute; left: 0; width: 100%; top: 994px; height: 40px;
    display: flex; justify-content: center; align-items: center; gap: 10px; font-size: 28px;
  }
  .footer-note svg { width: 40px; height: 40px; }
</style>
</head>
<body>
  <article class="menu-card">
    <div class="leaf-decoration" role="img" aria-label="Faint cannabis leaf watermark behind the price lists"></div>

    <svg class="frame" viewBox="0 0 462 1110" aria-hidden="true">
      <path d="M46 16 H416 A30 30 0 0 0 446 46 V1064 A30 30 0 0 0 416 1094 H46 A30 30 0 0 0 16 1064 V46 A30 30 0 0 0 46 16 Z"
            fill="none" stroke="var(--line)" stroke-width="2.5"/>
      <rect x="24" y="30" width="414" height="1050" fill="none" stroke="var(--line)" stroke-width="1.5" stroke-dasharray="8 6" opacity=".8"/>
    </svg>

    <h1 class="title"><span class="cap">A</span>MSTERDAM</h1>
    <div class="subtitle">MENU</div>
    <div class="rule rule--top"></div>

    <div class="section-head section-head--weed"><span class="label">WEED</span><span class="unit">PRICE P/G</span></div>
    <div class="head-line head-line--weed-a"></div>
    <div class="head-line head-line--weed-b"></div>
    <ul class="price-list price-list--weed">
      <li style="top:393px"><span class="name">Velotrine</span><span class="price">€16</span></li>
      <li style="top:433px"><span class="name">Cinderfox</span><span class="price">€14</span></li>
      <li style="top:473px"><span class="name" style="left:49px">Tide Rambler</span><span class="price">€14</span></li>
      <li style="top:512px"><span class="name" style="left:50px">Marigolden</span><span class="price">€16</span></li>
      <li style="top:552px"><span class="name">Grand Pelican</span><span class="price">€14</span></li>
      <li style="top:593px"><span class="name">Copper Comet</span><span class="price">€14</span></li>
    </ul>

    <div class="rule rule--middle"></div>

    <div class="section-head section-head--hash"><span class="label">HASH</span><span class="unit">PRICE P/G</span></div>
    <div class="head-line head-line--hash-a"></div>
    <div class="head-line head-line--hash-b"></div>
    <ul class="price-list price-list--hash">
      <li style="top:806px"><span class="name" style="left:45px">Baltic Ember</span><span class="price">€12</span></li>
      <li style="top:847px"><span class="name" style="left:44px">Harbor Velvet</span><span class="price" style="left:300px">€11</span></li>
      <li style="top:887px"><span class="name" style="left:45px">Plum Rova</span><span class="price">€14</span></li>
      <li style="top:929px"><span class="name" style="left:44px">Dusk Maple</span><span class="price">€10</span></li>
    </ul>

    <p class="footer-note">
      <svg viewBox="0 0 40 40" role="img" aria-label="No smoking">
        <rect x="9" y="18" width="20" height="5" rx="1" fill="var(--text)" opacity=".85"/>
        <rect x="26" y="18" width="4" height="5" fill="var(--accent)"/>
        <circle cx="20" cy="20" r="17" fill="none" stroke="var(--no-smoke)" stroke-width="3"/>
        <line x1="8" y1="8" x2="32" y2="32" stroke="var(--no-smoke)" stroke-width="3"/>
      </svg>
      <span>No cigarettes</span>
    </p>
  </article>
</body>
</html>
```